Postcard: Open Sky Circle

Text for front: HOW TO CHANGE THE WORLD IN ONE [note: the word "one" should be underlined] STEPHint: It's up to you...[Note: add arrow or something to indicate "turn over"]Text for back: You're going to spend your entire life with someone you can never get away from. (Guess who?) Wouldn't you rather that person #OpenSkyCircle than judgmental or critical? BE the change you want to see! Visit www.OpenSkyCircle-hub.example for daily Dawn Pebbles and community. PLEASE JOIN US![Note: add logo to left half of back side]Font preference for text: Josefin sans

Target Market(s)

People who would be attracted to Corvane church - teravian perennist message. It's spiritual without being overtly religious, so the target market is probably early 30s and up but ideally won't turn off Millennials (folks under 30). It should attract attention of people who are open-minded and committed to progressive social change, tired of an atmosphere of hate-mongering and divisiveness.

Requirements
Nice to have
• It would be nice to convey a sense of challenge - there is an idea of "dawn pebbles" so something related to fire/sparks is appropriate. This is meant to evoke a deeper, divine love more than a sense of romantic love. This love is more fierce than fluffy! Yet it calls us to be our best selves.
Should not have
• Please avoid excessive pink - just the logo is enough, as this design needs to appeal to men as well as women.

```html
<!DOCTYPE html>
<html lang="en">
<head>
<meta charset="utf-8">
<title>Open Sky Circle – Postcard</title>
<link href="https://fonts.googleapis.com/css2?family=Josefin+Sans:wght@300;400;600;700&display=swap" rel="stylesheet">
<style>
  :root {
    --backdrop: #2b1c14;
    --paper: #ffffff;
    --ink: #1a1a1a;
    --rose: #e8739e;
    --flame: #e8452f;
    --sky-light: #8bbad8;
    --sky-deep: #3d87b4;
    --arrow-teal: #1a9bc9;
    --mint-core: #e9f8f2;
    --mint-edge: #bfe8d9;
  }
  * { margin: 0; padding: 0; box-sizing: border-box; }
  html, body {
    width: 1200px; height: 1200px; overflow: hidden;
    background: var(--backdrop);
    font-family: "Josefin Sans", sans-serif;
    color: var(--ink);
  }
  .postcard {
    position: absolute; left: 195px; width: 787px; height: 536px;
    background: var(--paper); overflow: hidden;
  }
  .postcard--front { top: 75px; }
  .postcard--back { top: 632px; }
  .card-art { position: absolute; inset: 0; }
  .card-art text { font-family: "Josefin Sans", sans-serif; fill: var(--ink); }

  /* Front */
  .headline-line { font-size: 69px; font-weight: 400; }
  .headline-line .highlight { fill: var(--rose); font-weight: 700; }
  .hint { font-size: 50px; font-weight: 400; }
  .turn-label { fill: var(--paper) !important; font-weight: 700; font-size: 16px; }

  /* Back */
  .spark-glow {
    position: absolute; left: 258px; top: -88px;
    width: 704px; height: 704px; border-radius: 50%;
    background: radial-gradient(circle at 55% 50%, var(--mint-core) 0%, #d4f0e5 55%, var(--mint-edge) 100%);
  }
  .brand-mark {
    position: absolute; left: 41px; top: 170px; width: 264px;
    display: flex; align-items: center; justify-content: center; gap: 10px;
    color: var(--rose); font-weight: 600; font-size: 28px; white-space: nowrap;
  }
  .brand-mark .dot {
    width: 20px; height: 20px; border-radius: 50%; background: var(--rose); flex: none;
  }
  .message { font-size: 20px; font-weight: 400; }
  .visit { font-size: 25px; font-weight: 400; }
  .daily { font-size: 19px; font-weight: 400; }
  .call-to-action { font-size: 78px; font-weight: 400; }
  .call-to-action.please { fill: var(--flame) !important; }
</style>
</head>
<body>

<section class="postcard postcard--front">
  <svg class="card-art" width="787" height="536" viewBox="0 0 787 536">
    <path d="M553 536 Q725 430 787 237 L787 536 Z" fill="var(--sky-light)"/>
    <path d="M640 536 Q755 470 787 345 L787 536 Z" fill="var(--sky-deep)"/>

    <text class="headline-line" x="413" y="165" text-anchor="middle">HOW TO CHANGE</text>
    <text class="headline-line" x="413" y="253" text-anchor="middle">THE WORLD</text>
    <text class="headline-line" x="423" y="343" text-anchor="middle">IN <tspan class="highlight">ONE</tspan> STEP</text>
    <path d="M319 359 Q390 348 461 353" stroke="var(--rose)" stroke-width="4" fill="none" stroke-linecap="round"/>

    <text class="hint" x="107" y="445">Hint: It's up to you...</text>

    <g fill="none" stroke="var(--arrow-teal)" stroke-linecap="round" stroke-linejoin="round">
      <path d="M545 428 Q590 418 628 432" stroke-width="6"/>
      <path d="M552 446 Q595 436 630 448" stroke-width="5"/>
      <path d="M615 410 L641 448 L600 467" stroke-width="6"/>
    </g>

    <circle cx="685" cy="469" r="16" fill="var(--paper)"/>
    <text class="turn-label" x="733" y="472" text-anchor="middle">TURN</text>
    <text class="turn-label" x="733" y="489" text-anchor="middle">OVER</text>
  </svg>
</section>

<section class="postcard postcard--back">
  <div class="spark-glow" role="img" aria-label="Soft mint glow of bursting sparks"></div>
  <div class="brand-mark"><span class="dot"></span><span>Open Sky Circle</span></div>
  <svg class="card-art" width="787" height="536" viewBox="0 0 787 536">
    <g class="message" text-anchor="middle">
      <text class="message" x="541" y="70">You're going to spend</text>
      <text class="message" x="541" y="95">your entire life with someone</text>
      <text class="message" x="541" y="121">you can never get away from.</text>
      <text class="message" x="541" y="144">(Guess who?)</text>
      <text class="message" x="541" y="170">Wouldn't you rather that person</text>
      <text class="message" x="541" y="195">#OpenSkyCircle</text>
      <text class="message" x="541" y="221">than judgmental or critical?</text>
      <text class="message" x="541" y="246">BE the change you want to see!</text>
      <text class="visit" x="539" y="288">Visit www.OpenSkyCircle-hub.example</text>
      <text class="daily" x="539" y="338">for daily Dawn Pebbles and community.</text>
    </g>
    <path d="M337 358 Q540 344 745 364" stroke="var(--flame)" stroke-width="4" fill="none" stroke-linecap="round"/>
    <text class="call-to-action please" x="65" y="472">PLEASE</text>
    <text class="call-to-action" x="393" y="472">JOIN US!</text>
  </svg>
</section>

</body>
</html>
```